Tailbrook - eCommerce Design and Shopify Theme customisation

eCommerce Website Design - firstly with mockups then once we have chosen the design the successful designer will need to choose, purchase and customise a Shopify theme to match the design. We have a logo already designed and now want to create our web presence based on carrying up to 50 products on our website.
Target Market(s)
UK Pet Owners
Industry/Entity Type
Pet Shop
Requirements
Must have
- Design must be achievable using a customised Shopify theme - the successful designer will be responsible for the delivery of a working theme on our shopify website.
Should not have
- should not look cheap or have designs that aren't compatible or achievable with Shopify

```html
<!DOCTYPE html>
<html lang="en">
<head>
<meta charset="utf-8">
<title>Tailbrook – Pet Shop</title>
<link rel="stylesheet" href="https://fonts.googleapis.com/css2?family=Courgette&family=Poppins:wght@400;500;600&display=swap">
<style>
:root{
  --gold:#d5b23b;
  --gold-soft:#dcc05c;
  --ink:#2a2a2a;
  --dark:#262626;
  --grey:#f3f3f3;
  --line:#e2e2e2;
  --muted:#777;
  --red:#d0021b;
  --white:#fff;
}
*{box-sizing:border-box;margin:0;padding:0}
html,body{width:1200px;height:4455px;overflow:hidden}
body{position:relative;font-family:"Poppins",sans-serif;color:var(--ink);background:var(--white);font-size:14px}
.abs{position:absolute}
.script{font-family:"Courgette",cursive;font-weight:400}
.btn{position:absolute;display:flex;align-items:center;justify-content:center;border-radius:30px;font-size:13px;font-weight:500}
.btn-gold{background:var(--gold);color:var(--white)}
.btn-outline{border:2px solid var(--ink);color:var(--ink);background:transparent}
.btn-outline-white{border:2px solid var(--white);color:var(--white)}

/* header + hero */
.hero{position:absolute;left:0;top:0;width:1200px;height:660px;background:var(--grey)}
.menu{left:40px;top:36px;display:flex;align-items:center;gap:10px;font-size:12px;font-weight:500;letter-spacing:1px}
.logo{left:0;width:1200px;top:22px;display:flex;flex-direction:column;align-items:center;gap:4px}
.logo .mark{width:40px;height:40px;border-radius:50%;background:var(--gold)}
.logo .name{font-size:20px;font-weight:600;color:var(--ink)}
.header-icons{right:40px;top:34px;display:flex;gap:24px}
.hero .eyebrow{left:100px;top:266px;font-size:24px;color:var(--gold)}
.hero h1{left:100px;top:300px;font-size:44px;color:var(--gold)}
.hero .lead{left:100px;top:368px;width:300px;font-size:14px;line-height:1.45}
.hero-photo{left:540px;top:120px;width:620px;height:520px;border-radius:40% 40% 10px 10px;background:radial-gradient(ellipse at 40% 45%,#d99a52 0%,#c88a49 35%,#e7dccd 62%,var(--grey) 75%)}

/* categories */
.category{position:absolute;top:698px;width:534px;height:350px;overflow:hidden}
.category.cat{left:42px;background:linear-gradient(120deg,#6fc4b6,#89cdbf 55%,#b9b0a3)}
.category.dog{left:624px;background:linear-gradient(120deg,#4f4a45,#8c8479 50%,#d8d2c6)}
.category h3{position:absolute;left:34px;top:38px;font-size:22px;color:var(--white)}
.category p{position:absolute;left:34px;top:76px;width:220px;color:var(--white);font-size:13px;line-height:1.4}
.category .btn{left:34px;top:128px;width:186px;height:50px}

/* section title */
.section-title{position:absolute;left:0;width:1200px;text-align:center;font-size:28px;color:var(--ink)}
.arrows{position:absolute;right:42px;display:flex;gap:8px}
.arrows span{width:30px;height:30px;border-radius:50%;border:2px solid #999;display:flex;align-items:center;justify-content:center}
.arrows span.next{border-color:var(--gold)}

/* products */
.products{position:absolute;left:42px;width:1116px;display:flex;justify-content:space-between}
.product{width:258px;text-align:center}
.product .thumb{height:270px;border:1px solid var(--line);display:flex;align-items:center;justify-content:center;background:var(--white)}
.product .pack{width:120px;height:180px;border-radius:6px}
.product .pack.can{width:150px;height:110px;border-radius:14px}
.product .name{margin-top:14px;font-size:13px}
.product .old{font-size:12px;color:var(--muted);text-decoration:line-through}
.product .price{font-size:13px;color:var(--red);font-weight:600}

/* sale banner */
.sale{position:absolute;left:0;top:1640px;width:1200px;height:487px;background:var(--gold)}
.sale .frame{position:absolute;left:18px;top:18px;right:18px;bottom:18px;border:2px solid rgba(255,255,255,.8)}
.sale h2{position:absolute;left:100px;top:152px;font-size:44px;color:var(--white)}
.sale .amount{position:absolute;left:100px;top:214px;font-size:24px;font-weight:600;color:var(--red)}
.sale p{position:absolute;left:100px;top:250px;width:370px;color:var(--white);font-size:13px;line-height:1.4}
.sale .btn{left:100px;top:305px;width:186px;height:48px}
.sale-photo{position:absolute;left:540px;top:95px;width:560px;height:320px;border-radius:16px;background:linear-gradient(100deg,#e9a43a,#f1f1ec 35%,#9fbf7a 60%,#e7e3dc 80%,#c9b48b)}

/* testimonial */
.testimonial{position:absolute;left:42px;top:2706px;width:1116px;height:386px;background:linear-gradient(90deg,var(--gold) 0%,var(--gold-soft) 55%,#c9a948 100%);text-align:center;color:var(--white)}
.testimonial h3{position:absolute;left:0;right:0;top:78px;font-size:26px}
.testimonial .who{position:absolute;left:0;right:0;top:120px;font-size:16px;letter-spacing:1px}
.testimonial p{position:absolute;left:230px;right:230px;top:156px;font-size:13px;line-height:1.5}
.testimonial .quote{position:absolute;top:140px;font-size:60px;font-family:"Courgette",cursive;line-height:1}
.testimonial .stars{position:absolute;left:0;right:0;top:214px;font-size:18px;letter-spacing:4px}
.testimonial .btn{left:468px;top:258px;width:182px;height:48px}

/* blogs */
.blogs{position:absolute;left:42px;top:3202px;width:1116px;display:flex;justify-content:space-between}
.post{width:360px;height:392px;border:1px solid var(--line);padding:18px}
.post .photo{height:213px}
.post .meta{margin-top:24px;font-size:12px;color:var(--ink)}
.post .meta span{margin:0 10px;color:#aaa}
.post h4{margin-top:8px;font-size:13px;font-weight:500}
.post p{margin-top:4px;font-size:12px;line-height:1.4}
.post .more{margin-top:16px;font-size:11px;color:var(--muted)}

/* features */
.feature{position:absolute;top:3715px;width:350px;height:155px;display:flex;align-items:center;padding:0 36px;gap:18px;color:var(--white)}
.feature.dark{background:linear-gradient(90deg,#1f1f1f,#3a3a3a)}
.feature.gold{background:var(--gold)}
.feature h5{font-family:"Courgette",cursive;font-size:14px;font-weight:400}
.feature p{font-size:12px;line-height:1.4}

/* newsletter */
.newsletter h3{top:3918px;font-size:20px}
.newsletter-text{position:absolute;left:0;width:1200px;top:3952px;text-align:center;font-size:12px;line-height:1.45}
.subscribe{position:absolute;left:309px;top:3998px;width:484px;height:42px;border:1px solid var(--line);border-radius:30px;display:flex;align-items:center;padding-left:20px;font-size:11px;color:#999}
.subscribe .send{position:absolute;right:0;top:-1px;width:62px;height:42px;border-radius:30px;background:var(--gold);display:flex;align-items:center;justify-content:center}

/* footer */
.footer{position:absolute;left:42px;top:4090px;width:1116px;height:297px;background:var(--dark);color:var(--white)}
.footer .brand{position:absolute;left:40px;top:36px;display:flex;align-items:center;gap:10px;font-size:22px;font-weight:600}
.footer .brand i{width:36px;height:36px;border-radius:50%;background:var(--gold);display:block}
.footer .contact{position:absolute;left:40px;top:130px;font-size:12px;line-height:1.75;list-style:none}
.footer .contact li{display:flex;align-items:center;gap:8px}
.footer .col{position:absolute;top:36px;font-size:12px}
.footer .col h6{font-family:"Courgette",cursive;font-weight:400;font-size:13px;margin-bottom:14px}
.footer .col ul{list-style:none;line-height:1.85}
.footer .col li::before{content:"›";margin-right:10px}
.footer .social li::before{content:none}
.footer .social li{display:flex;align-items:center;gap:10px}
.footer .social li i{width:14px;height:14px;border-radius:50%;display:block}
.copyright{position:absolute;left:60px;top:4404px;font-size:12px}
.cards{position:absolute;right:42px;top:4400px;display:flex;gap:6px}
.cards span{width:48px;height:30px;border:1px solid #ccc;border-radius:3px;display:block}
</style>
</head>
<body>

<section class="hero">
  <div class="abs menu">
    <svg width="22" height="16" viewBox="0 0 22 16"><path d="M0 2h22M0 8h22M0 14h22" stroke="#2a2a2a" stroke-width="2"/></svg>
    MENU
  </div>
  <div class="abs logo"><span class="mark"></span><span class="name">Tailbrook</span></div>
  <div class="abs header-icons">
    <svg width="18" height="18" viewBox="0 0 18 18"><circle cx="7.5" cy="7.5" r="5.5" fill="none" stroke="#2a2a2a" stroke-width="2"/><path d="M12 12l5 5" stroke="#2a2a2a" stroke-width="2"/></svg>
    <svg width="18" height="18" viewBox="0 0 18 18"><circle cx="9" cy="5.5" r="4" fill="none" stroke="#2a2a2a" stroke-width="1.8"/><path d="M2 17c1-4 4-6 7-6s6 2 7 6" fill="none" stroke="#2a2a2a" stroke-width="1.8"/></svg>
    <svg width="18" height="18" viewBox="0 0 18 18"><path d="M9 16S1 11 1 5.5A4 4 0 0 1 9 4a4 4 0 0 1 8 1.5C17 11 9 16 9 16z" fill="none" stroke="#2a2a2a" stroke-width="1.8"/></svg>
    <svg width="18" height="18" viewBox="0 0 18 18"><path d="M1 2h3l2 10h9l2-7H5" fill="none" stroke="#2a2a2a" stroke-width="1.8"/><circle cx="7" cy="16" r="1.4" fill="#2a2a2a"/><circle cx="14" cy="16" r="1.4" fill="#2a2a2a"/></svg>
  </div>
  <div class="abs eyebrow script">Welcome To</div>
  <h1 class="abs script">All Pet Products</h1>
  <p class="abs lead">Lorem Ipsum is simply dummy text of the printing and typesetting industry.</p>
  <a class="btn btn-outline" style="left:100px;top:425px;width:188px;height:50px">Read More</a>
  <div class="abs hero-photo" role="img" aria-label="A ginger and white cat sitting beside a golden puppy with a bowl of dry pet food"></div>
</section>

<div class="category cat" role="img" aria-label="Long-haired cat lying on a mint green background">
  <h3 class="script">Cat Products</h3>
  <p>Lorem Ipsum is simply dummy text of the printing.</p>
  <a class="btn btn-gold">Shop Now&gt;&gt;</a>
</div>
<div class="category dog" role="img" aria-label="Small white fluffy dog running">
  <h3 class="script">Dog Products</h3>
  <p>Lorem Ipsum is simply dummy text of the printing.</p>
  <a class="btn btn-gold">Shop Now&gt;&gt;</a>
</div>

<h2 class="section-title script" style="top:1108px">Cat Products</h2>
<div class="arrows" style="top:1112px">
  <span><svg width="12" height="12" viewBox="0 0 12 12"><path d="M8 2L4 6l4 4" fill="none" stroke="#999" stroke-width="2"/></svg></span>
  <span class="next"><svg width="12" height="12" viewBox="0 0 12 12"><path d="M4 2l4 4-4 4" fill="none" stroke="#d5b23b" stroke-width="2"/></svg></span>
</div>
<div class="products" style="top:1165px">
  <div class="product"><div class="thumb"><div class="pack" role="img" aria-label="Bag of cat food" style="background:linear-gradient(160deg,#6b2c8c,#e7c12f 60%,#c0392b)"></div></div><div class="name">Product Name</div><div class="old">$00.00</div><div class="price">$00.00</div></div>
  <div class="product"><div class="thumb"><div class="pack" role="img" aria-label="Bag of cat food" style="background:linear-gradient(160deg,#e6a53b,#f4e3b5 55%,#b7812e)"></div></div><div class="name">Product Name</div><div class="old">$00.00</div><div class="price">$00.00</div></div>
  <div class="product"><div class="thumb"><div class="pack" role="img" aria-label="Bag of cat food" style="background:linear-gradient(160deg,#f0a21f,#e58a1a 60%,#b86410)"></div></div><div class="name">Product Name</div><div class="old">$00.00</div><div class="price">$00.00</div></div>
  <div class="product"><div class="thumb"><div class="pack can" role="img" aria-label="Tin of wet cat food" style="background:linear-gradient(180deg,#e0a33c,#f6efe1 45%,#d37a2a)"></div></div><div class="name">Product Name</div><div class="old">$00.00</div><div class="price">$00.00</div></div>
</div>
<a class="btn btn-gold" style="left:514px;top:1538px;width:186px;height:52px">Browse All</a>

<section class="sale">
  <div class="frame"></div>
  <h2 class="script">Save Up To 40%</h2>
  <div class="amount">$120.200</div>
  <p>Lorem Ipsum is simply dummy text of the printing and Food typesetting industry.</p>
  <a class="btn btn-outline-white">Shop Now &gt;&gt;</a>
  <div class="sale-photo" role="img" aria-label="Group of pet food bags, treats and tins"></div>
</section>

<h2 class="section-title script" style="top:2178px">Dog Products</h2>
<div class="arrows" style="top:2182px">
  <span><svg width="12" height="12" viewBox="0 0 12 12"><path d="M8 2L4 6l4 4" fill="none" stroke="#999" stroke-width="2"/></svg></span>
  <span class="next"><svg width="12" height="12" viewBox="0 0 12 12"><path d="M4 2l4 4-4 4" fill="none" stroke="#d5b23b" stroke-width="2"/></svg></span>
</div>
<div class="products" style="top:2240px">
  <div class="product"><div class="thumb"><div class="pack" role="img" aria-label="Bag of dog food" style="background:linear-gradient(160deg,#f0a21f,#f6c24a 55%,#2d5f9e)"></div></div><div class="name">Product Name</div><div class="old">$00.00</div><div class="price">$00.00</div></div>
  <div class="product"><div class="thumb"><div class="pack" role="img" aria-label="Bag of dog food" style="background:linear-gradient(160deg,#3b2a20,#8a5a2c 55%,#4b7a3a)"></div></div><div class="name">Product Name</div><div class="old">$00.00</div><div class="price">$00.00</div></div>
  <div class="product"><div class="thumb"><div class="pack" role="img" aria-label="Bag of dog food" style="background:linear-gradient(160deg,#1c1c1c,#2d2d2d 60%,#b89a4a)"></div></div><div class="name">Product Name</div><div class="old">$00.00</div><div class="price">$00.00</div></div>
  <div class="product"><div class="thumb"><div class="pack" role="img" aria-label="Bag of dog food" style="background:linear-gradient(160deg,#16244a,#22356a 60%,#b89a4a)"></div></div><div class="name">Product Name</div><div class="old">$00.00</div><div class="price">$00.00</div></div>
</div>
<a class="btn btn-gold" style="left:514px;top:2614px;width:186px;height:48px">Browse All</a>

<section class="testimonial" role="img" aria-label="Faded photo of a dog resting, under a golden tint">
  <h3 class="script">Our Clients Says</h3>
  <div class="who">MARA ELLISON</div>
  <span class="quote" style="left:170px">&ldquo;</span>
  <p>Lorem Ipsum is simply dummy text of the printing and typesetting industry. Lorem Ipsum has been the industry's standard dummy text ever since the 1500s.</p>
  <span class="quote" style="right:170px">&rdquo;</span>
  <div class="stars">★★★★★</div>
  <a class="btn btn-outline-white">KNOWN MORE</a>
</section>

<h2 class="section-title script" style="top:3137px">Blogs</h2>
<div class="arrows" style="top:3141px">
  <span><svg width="12" height="12" viewBox="0 0 12 12"><path d="M8 2L4 6l4 4" fill="none" stroke="#999" stroke-width="2"/></svg></span>
  <span class="next"><svg width="12" height="12" viewBox="0 0 12 12"><path d="M4 2l4 4-4 4" fill="none" stroke="#d5b23b" stroke-width="2"/></svg></span>
</div>
<div class="blogs">
  <article class="post"><div class="photo" role="img" aria-label="Kitten sleeping under a white blanket" style="background:linear-gradient(135deg,#eef1f4,#cfd6dd 60%,#a7a49e)"></div><div class="meta">By Admin<span>|</span>01 May, 2019</div><h4>What is Lorem Ipsum?</h4><p>Lorem Ipsum is simply dummy the printing a typesetting industry.</p><div class="more">Continue.. ›</div></article>
  <article class="post"><div class="photo" role="img" aria-label="Smiling dog sitting on green grass" style="background:linear-gradient(180deg,#5c7c3a,#8fb05a 55%,#4e6e2a)"></div><div class="meta">By Admin<span>|</span>01 May, 2019</div><h4>What is Lorem Ipsum?</h4><p>Lorem Ipsum is simply dummy the printing a typesetting industry.</p><div class="more">Continue.. ›</div></article>
  <article class="post"><div class="photo" role="img" aria-label="Grey puppy chewing a red toy" style="background:linear-gradient(135deg,#f1f1f1,#8a8a8e 55%,#c0392b)"></div><div class="meta">By Admin<span>|</span>01 May, 2019</div><h4>What is Lorem Ipsum?</h4><p>Lorem Ipsum is simply dummy the printing a typesetting industry.</p><div class="more">Continue.. ›</div></article>
</div>
<a class="btn btn-gold" style="left:514px;top:3618px;width:186px;height:47px">View More&gt;&gt;</a>

<div class="feature dark" style="left:42px">
  <svg width="40" height="28" viewBox="0 0 40 28"><path d="M1 3h24v17H1zM25 9h8l6 6v5H25z" fill="none" stroke="#fff" stroke-width="2"/><circle cx="9" cy="23" r="3" fill="#262626" stroke="#fff" stroke-width="2"/><circle cx="31" cy="23" r="3" fill="#262626" stroke="#fff" stroke-width="2"/></svg>
  <div><h5>Free Shipping Worldwide</h5><p>On Order<br>Over $150 7 Days a week</p></div>
</div>
<div class="feature gold" style="left:422px">
  <svg width="34" height="32" viewBox="0 0 34 32"><path d="M4 18v-3a13 13 0 0 1 26 0v3" fill="none" stroke="#fff" stroke-width="2"/><rect x="2" y="17" width="6" height="10" rx="2" fill="#fff"/><rect x="26" y="17" width="6" height="10" rx="2" fill="#fff"/></svg>
  <div><h5>24/7 Customer Service</h5><p>Call us 24/7<br>0116 000 4821</p></div>
</div>
<div class="feature dark" style="left:805px">
  <svg width="36" height="30" viewBox="0 0 36 30"><path d="M2 12L16 2l18 14-14 12z" fill="none" stroke="#fff" stroke-width="2"/><circle cx="14" cy="9" r="2" fill="#fff"/></svg>
  <div><h5>Save 10%</h5><p>with the Tailbrook Card</p></div>
</div>

<div class="newsletter">
  <h3 class="section-title script">Subscribe To Our Newsletter</h3>
</div>
<p class="newsletter-text">Subscribe to our newsletter so we can spam you<br>with offers and discounts.</p>
<div class="subscribe">Your E-Mail
  <span class="send"><svg width="18" height="16" viewBox="0 0 18 16"><path d="M1 8L17 1l-4 14-4-5z" fill="#fff"/></svg></span>
</div>

<footer class="footer">
  <div class="brand"><i></i>Tailbrook</div>
  <ul class="contact">
    <li><svg width="10" height="14" viewBox="0 0 10 14"><path d="M5 0a5 5 0 0 1 5 5c0 4-5 9-5 9S0 9 0 5a5 5 0 0 1 5-5z" fill="#fff"/></svg>48 Orchard Lane</li>
    <li style="padding-left:18px">Harrowgate, UK</li>
    <li><svg width="12" height="12" viewBox="0 0 12 12"><path d="M2 0l3 3-1.5 2a7 7 0 0 0 3.5 3.5L9 7l3 3-2 2C5 12 0 7 0 2z" fill="#fff"/></svg>(44)-2017-440-118</li>
    <li><svg width="12" height="10" viewBox="0 0 12 10"><rect width="12" height="10" fill="#fff"/><path d="M0 0l6 5 6-5" fill="none" stroke="#262626"/></svg>hello@tailbrook.co</li>
  </ul>
  <div class="col" style="left:330px"><h6>Quick link</h6><ul><li>My Account</li><li>Cart Page</li><li>Personal info</li><li>wishlist</li><li>Gifts</li><li>Terms and Conditions</li></ul></div>
  <div class="col" style="left:560px"><h6>Quick link</h6><ul><li>Home</li><li>Dog</li><li>Cat</li><li>Shop</li><li>Blog</li><li>Contact us</li></ul></div>
  <div class="col social" style="left:840px"><h6>Follow us on our Social Media</h6><ul>
    <li><i style="background:#3b5998"></i>Community</li>
    <li><i style="background:#c13584"></i>Gallery</li>
    <li><i style="background:#1da1f2"></i>Updates</li>
    <li><i style="background:#0077b5"></i>Network</li>
  </ul></div>
</footer>

<p class="copyright">Copyright © 2019 Tailbrook. All Rights Reserved.</p>
<div class="cards"><span></span><span></span><span></span><span></span></div>

</body>
</html>
```